Language School website design

Harborline Languages is looking for a designer who can "spice up" our website under development with a new cascading style sheet (CSS) and re-design our logo and start branding for business cards etc.
It will be up to the designer to come up with a layout in photoshop that pleases the team after agreement on the static photoshop file, provide a CSS file and all needed objects in a ZIP file
The designer is to deliver a CSS that doesn't require changes to the HTML content or structure. You are to base the design and get input on title length and structure of the site on
www.harborline-languages.example.
Please refer to the contents of the various pages for developing the CSS file.
If we are happy with the work, we will use the designer for brochure design, branding, etc.
Updates

Project Deadline Extended
Reason: Programming was delayed, but design is now urgent.

Project Deadline Extended
Reason: Programmer delayed in finishing programming

Please send all information to martin@harborline-languages.example

A design we like is www.vostrel.example

Blue is a main colour on the site.

We will provide our photos and PDFs

Thanks

Target Market(s)

Spanish speaking companies

Industry/Entity Type

Business

Requirements
Should not have
• Old style fonts. Use of people in a classroom.

```html
<!DOCTYPE html>
<html lang="es">
<head>
<meta charset="utf-8">
<title>Harborline Languages</title>
<link rel="stylesheet" href="https://fonts.googleapis.com/css2?family=Carlito:ital,wght@0,400;0,700;1,400;1,700&display=swap">
<style>
:root{
  --blue:#0b8ac9;
  --navy:#0f2a4a;
  --ink:#1c1c1c;
  --muted:#444;
  --page:#eef0ef;
  --white:#fff;
}
*{box-sizing:border-box;margin:0;padding:0}
html,body{width:1200px;height:1200px;overflow:hidden}
body{position:relative;font-family:"Carlito",sans-serif;color:var(--ink);
  background:var(--page);
  background-image:linear-gradient(90deg,rgba(0,0,0,.025) 1px,transparent 1px),linear-gradient(rgba(0,0,0,.025) 1px,transparent 1px);
  background-size:60px 60px}
.abs{position:absolute}
.header{position:absolute;left:0;top:0;width:1200px;height:440px;background:var(--white);border-top:2px solid var(--blue)}
.lang-bar{left:815px;top:0;width:255px;height:28px;background:var(--blue);color:var(--white);font-size:12px;line-height:28px;padding-left:10px;white-space:nowrap}
.brand{left:215px;top:66px;display:flex;align-items:center;gap:10px}
.brand-mark{width:20px;height:20px;background:var(--blue)}
.brand-name{font-size:24px;color:var(--navy)}
.nav{left:508px;top:77px;display:flex;gap:22px;font-size:13px;color:var(--navy);white-space:nowrap}
.nav span::before{content:"›";margin-right:5px;font-size:10px}
.phone-note{left:120px;top:190px;width:266px;text-align:right;font-style:italic;color:var(--blue);font-size:14px;line-height:17px}
.offer-title{left:505px;top:158px;width:405px;text-align:right;font-style:italic;color:var(--navy);font-size:22px;font-weight:400}
.offer-rule{left:509px;top:187px;width:401px;height:1px;background:var(--blue)}
.offer-text{left:505px;top:190px;width:405px;text-align:right;font-style:italic;color:var(--blue);font-size:13.5px;line-height:17px}
.product-name{left:932px;top:168px;color:var(--navy);font-size:34px;line-height:40px}
.tiles{left:130px;top:240px;display:flex;gap:10px}
.tile{position:relative;width:180px;height:180px;background:var(--blue);color:var(--white)}
.tile-photo{position:absolute;left:5px;top:5px;width:170px;height:132px}
.tile-label{position:absolute;left:0;top:0;background:var(--blue);padding:4px 16px 3px 6px;font-size:13px;width:110px}
.tile-caption{position:absolute;left:4px;top:144px;font-size:12px;line-height:14px;width:170px}
.card{left:131px;top:461px;width:938px;height:598px;background:var(--white);border:2px solid #dfe1e1}
.side-photo{position:absolute;width:150px;height:100px;box-shadow:0 0 2px rgba(0,0,0,.3)}
.side-title{position:absolute;color:var(--blue);font-size:13px;line-height:17px;width:130px;font-weight:400}
.side-text{position:absolute;font-size:11.5px;line-height:14.5px;width:135px}
.main-text{position:absolute;left:319px;width:379px;font-size:11.3px;line-height:14.4px;text-align:justify;text-indent:36px}
.checks{position:absolute;left:340px;top:166px;list-style:none;font-style:italic;font-weight:700;color:var(--navy);font-size:13px;line-height:17px}
.checks li{display:flex;align-items:center;gap:6px}
.box-title{position:absolute;left:718px;width:180px;background:var(--blue);color:var(--white);font-size:12.5px;padding:2px 10px;height:19px;font-weight:400}
.box-text{position:absolute;left:719px;width:212px;font-size:11.5px;line-height:14.5px}
.footer-rule{position:absolute;left:9px;top:455px;width:918px;height:2px;background:var(--blue)}
.footer-links,.footer-info{position:absolute;top:468px;font-size:11.5px;color:var(--muted);white-space:nowrap}
.footer-links{left:9px}
.footer-info{right:9px}
</style>
</head>
<body>
<header class="header">
  <div class="abs lang-bar">Seleccione el idioma:&nbsp; Spanish / English / Catalan</div>
  <div class="abs brand"><span class="brand-mark"></span><span class="brand-name">Harborline Languages</span></div>
  <nav class="abs nav"><span>HOME</span><span>GO! CLASSES</span><span>GO! TRAINING</span><span>TRANSLATIONS</span><span>GO! CLUB</span><span>CONTACT</span></nav>
  <p class="abs phone-note">Contact Harborline Languages every working day in Barcelona on: +34 931 555 014</p>
  <svg class="abs" style="left:392px;top:184px" width="26" height="38" viewBox="0 0 26 38"><path d="M13 2 L24 15 H17 V36 H9 V15 H2 Z" fill="none" stroke="#0b8ac9" stroke-width="1.5"/></svg>
  <h1 class="abs offer-title">Harborline Languages te ofrece</h1>
  <div class="abs offer-rule"></div>
  <p class="abs offer-text">Cursos de inglés diseñados especialmente para tu sector y adaptados a las necesidades de tu empresa.</p>
  <div class="abs product-name">GO</div>
  <div class="abs tiles">
    <div class="tile"><div class="tile-photo" role="img" aria-label="Velero navegando en mar abierto" style="background:linear-gradient(#8fb6d6,#2d5f8d)"></div><div class="tile-label">YACHTING.</div><p class="tile-caption">Para el sector náutico-deportivo</p></div>
    <div class="tile"><div class="tile-photo" role="img" aria-label="Grúa cargando contenedores en un puerto" style="background:linear-gradient(#5b8fc4,#9a6a4c)"></div><div class="tile-label">MARITIME.</div><p class="tile-caption">Para el sector marítimo y naval</p></div>
    <div class="tile"><div class="tile-photo" role="img" aria-label="Andamios de una obra al atardecer" style="background:linear-gradient(#4a7596,#c9ccc8 70%,#333)"></div><div class="tile-label">CONSTRUCTION.</div><p class="tile-caption">Para el sector de la construcción</p></div>
    <div class="tile"><div class="tile-photo" role="img" aria-label="Engranajes metálicos azules" style="background:linear-gradient(135deg,#1e3f63,#6fa7cf)"></div><div class="tile-label">ENGINEERING.</div><p class="tile-caption">Para el sector de la ingeniería</p></div>
    <div class="tile"><div class="tile-photo" role="img" aria-label="Monedas y gráfico ascendente ante rascacielos" style="background:linear-gradient(#a9d3ef,#2a6a9e)"></div><div class="tile-label">FINANCE.</div><p class="tile-caption">Para el sector económico-financiero</p></div>
  </div>
</header>

<main class="abs card">
  <div class="side-photo" style="left:7px;top:7px;background:linear-gradient(135deg,#5f8fb3,#d7e4ee)" role="img" aria-label="Teléfonos en un vestíbulo de oficinas"></div>
  <h2 class="side-title" style="left:168px;top:6px">SESIONES TELEFÓNICAS.</h2>
  <p class="side-text" style="left:168px;top:42px">¡Aprende el idioma cuando quieras y desde donde quier</p>
  <div class="side-photo" style="left:7px;top:117px;background:linear-gradient(135deg,#3a3a40,#c9a06a)" role="img" aria-label="Patrón de sastre con cinta métrica"></div>
  <h2 class="side-title" style="left:168px;top:116px">A MEDIDA.</h2>
  <p class="side-text" style="left:168px;top:135px;width:132px">Diseñaremos aquello que mejor se adapte a vuestro perfil</p>

  <p class="main-text" style="top:7px">Di que sí (mejor dicho, GO) a nuestros cursos específicos de inglés, diseñados y adaptados para tu sector: Náutico, Marítimo, Económico-Financiero, Ingeniería, Construcción. En tu empresa, a la hora que te vaya mejor, en las fechas que más te convengan, y con los contenidos que tú elijas. Inglés adaptado para tu empresa. Clases presenciales, sesiones telefónicas, o ambas. Además, nuestra sección de desarrollo profesional ofrece cursillos de English for Business y cursos monográficos. Nuestro equipo de profesores está formado por profesionales nativos y titulados, además de ser expertos en tu sector. Y si necesitas traducciones, nuestro equipo de especialistas te puede ayudar.</p>
  <ul class="checks">
    <li><svg width="9" height="8" viewBox="0 0 9 8"><path d="M1 4 L3.5 7 L8 1" fill="none" stroke="#0f2a4a" stroke-width="1.8"/></svg>Tu sector</li>
    <li><svg width="9" height="8" viewBox="0 0 9 8"><path d="M1 4 L3.5 7 L8 1" fill="none" stroke="#0f2a4a" stroke-width="1.8"/></svg>Tu empresa</li>
    <li><svg width="9" height="8" viewBox="0 0 9 8"><path d="M1 4 L3.5 7 L8 1" fill="none" stroke="#0f2a4a" stroke-width="1.8"/></svg>Tus estudios de inglés</li>
  </ul>
  <p class="main-text" style="top:233px;height:101px;overflow:hidden">Los cursos de inglés GO son únicos por su contenido específico del sector. Dinos en que sector trabajas y nos adaptamos a tus necesidades. Además del inglés general, cada alumno aprende el inglés necesario para la comunicación diaria con sus clientes, proveedores y otros colaboradores. Elige entre cursos presenciales en tu empresa, con una duración de 30, 50 ó 80 horas, packs de clases telefónicas, con total flexibilidad de horarios, o bien una combinación de las dos modalidades.&nbsp; La Fundación Formativa para la formación continua bonifica estos cursos para empresas.</p>

  <h3 class="box-title" style="top:10px">CLASES PRESENCIALES</h3>
  <p class="box-text" style="top:34px">In-company, a la hora que te vaya mejor, en las fechas que más te convengan, y con los contenidos que tú elijas.</p>
  <h3 class="box-title" style="top:100px">CURSOS MONOGRAFICOS</h3>
  <p class="box-text" style="top:124px">Dirigidos a profesionales que deseen profundizar ciertos aspectos del idioma inglés.</p>

  <div class="footer-rule"></div>
  <p class="footer-links">Legal | Privacy | About us | FAQ</p>
  <p class="footer-info">Harborline Languages – www.harborline-languages.example – info@harborline-languages.example – T: 931 555 014</p>
</main>
</body>
</html>
```